Chiropractor needs a snazzy business card

Business card for a chiropractic office.
Office treats patients of all ages.
Focus is on a natural lifestyle.
Colors can include the logo colors as well as white and a little orange.
Ideally the card would have something chiropractic related such as a spine.

The back of the card should have a items for making appointments (date, times....)

```html
<!DOCTYPE html>
<html lang="en">
<head>
<meta charset="utf-8">
<title>Meridian Chiropractic – Business Card</title>
<link href="https://fonts.googleapis.com/css2?family=Cinzel:wght@400&family=Open+Sans:wght@400&display=swap" rel="stylesheet">
<style>
  :root {
    --navy: #2b4f7e;
    --navy-faint: #c3d2e4;
    --green: #5cb54a;
    --orange: #f7ae77;
    --orange-soft: #fde6d3;
    --ink: #5a5a5a;
    --ink-dark: #2c2c2c;
    --rule: #8a8a8a;
    --paper: #ffffff;
    --canvas: #ffffff;
  }
  * { box-sizing: border-box; margin: 0; padding: 0; }
  html, body {
    width: 1021px; height: 1200px; overflow: hidden;
    background: var(--canvas);
  }
  .sheet { position: relative; width: 1021px; height: 1200px; }

  .card {
    position: absolute; left: 0; width: 1021px;
    background: var(--paper);
    border: 1px solid var(--rule);
    overflow: hidden;
  }
  .card--front { top: 0; height: 590px; }
  .card--back { top: 610px; height: 590px; }

  /* Front */
  .brand {
    position: absolute; left: 38px; top: 36px;
    font-family: "Cinzel", serif; font-weight: 400;
    color: var(--navy); line-height: 1;
  }
  .brand__name { display: block; font-size: 78px; letter-spacing: 1px; }
  .brand__trade { display: block; font-size: 45px; letter-spacing: 6px; margin-top: 10px; }

  .spine-art {
    position: absolute; right: 0; bottom: 0; width: 520px; height: 590px;
  }

  .info {
    position: absolute; left: 44px;
    border-left: 6px solid var(--green);
    padding-left: 25px;
    font-family: "Open Sans", sans-serif;
    color: var(--ink);
  }
  .info--address { top: 239px; font-size: 23px; line-height: 35px; padding-top: 2px; padding-bottom: 2px; }
  .info--contact { top: 419px; font-size: 25px; line-height: 37px; padding-left: 31px; padding-top: 2px; padding-bottom: 2px; }

  /* Back */
  .watermark {
    position: absolute; left: 84px; top: 175px; width: 860px;
    font-family: "Cinzel", serif; font-weight: 400;
    color: var(--navy-faint); line-height: 1; text-align: center;
  }
  .watermark__name { display: block; font-size: 124px; letter-spacing: 2px; }
  .watermark__trade { display: block; font-size: 82px; letter-spacing: 8px; margin-top: 4px; }

  .appointment__title {
    position: absolute; left: 0; right: 0; top: 66px;
    text-align: center;
    font-family: "Cinzel", serif; font-weight: 400;
    font-size: 45px; letter-spacing: 2px;
    color: var(--ink-dark);
  }
  .field {
    position: absolute; left: 91px; width: 827px;
    display: flex; align-items: baseline;
    font-family: "Open Sans", sans-serif;
    font-size: 32px; color: var(--ink-dark);
  }
  .field__label { white-space: pre; }
  .field__line {
    flex: 1; height: 0;
    border-bottom: 2px dotted var(--ink-dark);
    margin-left: 2px;
  }
  .field--name { top: 150px; }
  .field--address { top: 236px; }
  .field--address-2 { top: 320px; }
  .field--date { top: 408px; }
  .field--times { top: 495px; }
</style>
</head>
<body>
<main class="sheet">

  <section class="card card--front" aria-label="Card front">
    <svg class="spine-art" viewBox="0 0 520 590" role="img" aria-label="Stylised orange spine illustration of curved vertebrae">
      <defs>
        <radialGradient id="spineGlow" cx="75%" cy="55%" r="70%">
          <stop offset="0%" stop-color="#f7ae77"/>
          <stop offset="60%" stop-color="#f9c39a"/>
          <stop offset="100%" stop-color="#ffffff"/>
        </radialGradient>
      </defs>
      <rect x="0" y="0" width="520" height="590" fill="url(#spineGlow)"/>
    </svg>

    <h1 class="brand">
      <span class="brand__name">MERIDIAN</span>
      <span class="brand__trade">CHIROPRACTIC</span>
    </h1>

    <address class="info info--address" style="font-style:normal">
      Address<br>
      Samle Text<br>
      xxxxxxxxxxxxxxxxxxxxxxxxxxxxx
    </address>

    <div class="info info--contact">
      tel.: +00 (000) 000-00-00<br>
      fax: +00 (000) 000-00-00<br>
      E-mail:
    </div>
  </section>

  <section class="card card--back" aria-label="Card back">
    <div class="watermark" aria-hidden="true">
      <span class="watermark__name">MERIDIAN</span>
      <span class="watermark__trade">CHIROPRACTIC</span>
    </div>

    <h2 class="appointment__title">Appointment Details</h2>

    <div class="field field--name"><span class="field__label">Patient  Name:</span><span class="field__line"></span></div>
    <div class="field field--address"><span class="field__label">Address:</span><span class="field__line"></span></div>
    <div class="field field--address-2"><span class="field__line"></span></div>
    <div class="field field--date"><span class="field__label">Date:</span><span class="field__line"></span></div>
    <div class="field field--times"><span class="field__label">Times:</span><span class="field__line"></span></div>
  </section>

</main>
</body>
</html>
```